Cannabis company needs an e-commerce website

Our retail cannabis company Harbor Velvet needs a fully functioning e-commerce website optimized for SEO. We want the website to have the appeal and sophistication of a cigar lounge/boutique coffee shop highlighting our high-end artisanal products. It should have the ability to categorize and search for products based on tags. Our initial number of SKUs will be about 25, but that will grow as the business grows.

Target Market(s)

Online retail cannabis users

Industry/Entity Type

Cannabis

Coding

Coded - Design and coding required

Number of Pages Required

5+ page

Font styles to use
Sans Serif

Requirements
Must have
• - Age confirmation (19+) confirmation popup
- Very simple and easy method of purchasing based on different product sizes
- Search functionality based on tags etc. of the products
- Similar functionality to the following websites:
1) https://www.pinemarshleafco.com/
2) https://amberguild.io/
3) https://florivexa.org/
4) https://sagetrellis.com/
- Similar look to the following websites:
1) https://layoutgrove.net/item/dorvik-snuff-store-theme/48203716
2) https://www.stemcrest.ca/
3) https://northdunemade.org/
4) https://wellbrookflorals.com/

```html
<!DOCTYPE html>
<html lang="en">
<head>
<meta charset="utf-8">
<title>Harbor Velvet — Traditional Cannabis Craftsmanship</title>
<link rel="stylesheet" href="https://fonts.googleapis.com/css2?family=Barlow+Condensed:wght@300;400;600&display=swap">
<style>
:root{
  --ink:#000;
  --tan:#b8865b;
  --tan-soft:#a87a52;
  --bronze:#7b5132;
  --white:#fff;
  --text-dark:#1a1a1a;
  --icon:#9a8a7c;
  --footer-head:#d6a57a;
  --footer-chip:#d6b394;
}
*{box-sizing:border-box;margin:0;padding:0}
html,body{width:1200px;height:3905px;overflow:hidden;background:var(--ink)}
body{position:relative;font-family:"Barlow Condensed",sans-serif;color:var(--tan)}
.abs{position:absolute}

/* hero */
.hero{left:0;top:0;width:1200px;height:818px;background:linear-gradient(180deg,#141110 0%,#2a2420 38%,#221d1a 62%,#0a0807 100%)}
.brand{left:95px;top:66px;display:flex;align-items:center;gap:10px;font-size:36px;font-weight:600;letter-spacing:1px;color:var(--tan);text-transform:uppercase;line-height:1}
.brand-mark{width:14px;height:14px;background:var(--tan)}
.nav{left:408px;top:84px;font-size:15px;font-weight:600;color:var(--tan);letter-spacing:.3px}
.nav span{position:absolute;white-space:nowrap}
.cart-count{left:1088px;top:20px;width:20px;height:20px;border-radius:50%;background:#fff;color:#000;font-size:11px;font-weight:600;text-align:center;line-height:20px}
.hero-title{left:201px;top:272px;text-transform:uppercase;line-height:1;white-space:nowrap}
.hero-title .lead{display:block;font-size:64px;font-weight:300;padding-left:60px}
.hero-title .main{display:block;font-size:78px;font-weight:600;margin-top:4px}

.feature{top:591px;width:332px;height:223px;background:linear-gradient(170deg,#3a3029,#1c1612 75%)}
.feature-frame{position:absolute;left:13px;top:15px;right:13px;bottom:15px;border:1px solid var(--tan-soft);text-align:center;text-transform:uppercase;padding-top:50px}
.feature h3{font-size:36px;font-weight:600;line-height:1}
.feature p{font-size:21px;font-weight:400;line-height:26px;margin-top:4px}

/* section titles */
.section-title{left:0;width:1200px;text-align:center;text-transform:uppercase;line-height:1}
.section-title .kicker{display:block;font-size:34px;font-weight:300}
.section-title .kicker.mixed{text-transform:none}
.section-title .head{display:block;font-size:44px;font-weight:600;margin-top:6px}

/* product cards */
.grid{left:92px;width:1016px;display:grid;grid-template-columns:repeat(4,1fr);gap:20px}
.card{position:relative;height:325px;background:var(--white)}
.card-photo{position:absolute;left:24px;right:24px;top:20px;height:200px}
.card-name{position:absolute;left:0;right:0;top:236px;text-align:center;font-size:17px;font-weight:400;color:var(--tan);text-transform:uppercase;letter-spacing:.3px}
.card-price{position:absolute;left:0;right:0;top:259px;text-align:center;font-size:17px;color:var(--text-dark)}
.add-cart{position:absolute;right:12px;bottom:10px;width:34px;height:34px;border-radius:50%;background:var(--tan);display:flex;align-items:center;justify-content:center}
.tone-wood{background:linear-gradient(180deg,#fff 0%,#f3e3d6 50%,#fff 100%)}
.tone-cigar{background:linear-gradient(180deg,#fff 0%,#efe4da 50%,#fff 100%)}
.tone-pale{background:linear-gradient(180deg,#fff 0%,#f1f1f1 50%,#fff 100%)}
.tone-berry{background:linear-gradient(180deg,#fff 0%,#f1e1e3 50%,#fff 100%)}
.tone-leaf{background:linear-gradient(180deg,#fff 0%,#ecedde 50%,#fff 100%)}
.tone-amber{background:linear-gradient(180deg,#fff 0%,#f6e5cf 50%,#fff 100%)}
.tone-sage{background:linear-gradient(180deg,#fff 0%,#e6ede6 50%,#fff 100%)}
.tone-char{background:linear-gradient(180deg,#fff 0%,#e4e4e4 50%,#fff 100%)}

/* vape feature */
.vape-photo{left:485px;top:1756px;width:715px;height:579px;background:linear-gradient(100deg,#0a0807 0%,#2c2723 40%,#3a342f 65%,#1e1a17 100%)}
.vape-copy{left:92px;top:1858px;width:360px}
.vape-copy h2{font-size:48px;line-height:48px;font-weight:400}
.vape-copy h2 strong{font-weight:600;display:block}
.vape-copy p{font-size:18px;line-height:30.5px;font-weight:400;margin-top:30px}

/* roots */
.roots{left:0;top:2919px;width:1200px;height:573px;background:linear-gradient(90deg,#1b120c,#2a1c12 50%,#150e09)}
.roots-video{left:92px;top:3024px;width:491px;height:358px;border:1px solid var(--tan-soft);background:linear-gradient(135deg,#4a3422,#2a1c12 55%,#140d08)}
.play{position:absolute;left:192px;top:125px;width:106px;height:106px;border:2px solid #fff;border-radius:50%;display:flex;align-items:center;justify-content:center}
.roots-copy{left:673px;top:3036px;width:420px}
.roots-copy h2{font-size:38px;font-weight:300;line-height:38px;text-transform:uppercase}
.roots-copy h2 strong{display:block;font-size:46px;font-weight:600;line-height:48px}
.roots-copy p{font-size:18px;line-height:30.5px;margin-top:16px}

/* footer */
.footer{left:0;top:3492px;width:1200px;height:413px;background:var(--bronze);color:#2a1a0e}
.footer h4{position:absolute;top:82px;font-size:24px;font-weight:400;color:var(--footer-head);text-transform:uppercase}
.footer-about{position:absolute;left:92px;top:128px;width:370px;font-size:14px;line-height:22px}
.contact{position:absolute;left:550px;font-size:14px;display:flex;align-items:center;gap:16px}
.news{position:absolute;left:860px;top:128px;width:260px;font-size:14px;line-height:20px}
.signup{position:absolute;left:860px;top:184px;width:74px;height:32px;background:var(--footer-chip);color:#3a2414;font-size:14px;text-align:center;line-height:32px}
.socials{position:absolute;left:860px;top:263px;display:flex;gap:14px}
.socials span{width:34px;height:34px;border-radius:50%;background:var(--footer-chip)}
.copyright{position:absolute;left:92px;top:278px;font-size:14px}
</style>
</head>
<body>

<section class="abs hero" role="img" aria-label="Black and white photograph of a man exhaling smoke from a pipe"></section>

<div class="abs brand"><span class="brand-mark"></span>Harbor Velvet</div>

<nav class="abs nav" aria-label="Main">
  <span style="left:0">FLOWER</span>
  <span style="left:91px">SALE</span>
  <span style="left:165px">EDIBLES</span>
  <span style="left:263px">VAPES</span>
  <span style="left:350px">CONCENTRATES</span>
  <span style="left:512px">CBD</span>
  <span style="left:581px">PACKS</span>
  <span style="left:654px">MORE</span>
</nav>

<div class="utility">
  <svg class="abs" style="left:891px;top:33px" width="18" height="20" viewBox="0 0 18 20" fill="#9a8a7c"><circle cx="9" cy="5" r="5"/><path d="M0 20c0-6 4-8 9-8s9 2 9 8z"/></svg>
  <svg class="abs" style="left:968px;top:34px" width="20" height="18" viewBox="0 0 20 18" fill="#9a8a7c"><path d="M10 18 1.5 9.5A5 5 0 0 1 10 3a5 5 0 0 1 8.5 6.5z"/></svg>
  <svg class="abs" style="left:1028px;top:34px" width="20" height="18" viewBox="0 0 20 18" fill="none" stroke="#9a8a7c" stroke-width="2"><path d="M2 13V10a8 8 0 0 1 16 0v3"/><rect x="1" y="11" width="4" height="6" fill="#9a8a7c"/><rect x="15" y="11" width="4" height="6" fill="#9a8a7c"/></svg>
  <svg class="abs" style="left:1078px;top:33px" width="22" height="20" viewBox="0 0 22 20" fill="#9a8a7c"><path d="M0 1h4l3 11h12l3-9H6" stroke="#9a8a7c" stroke-width="2" fill="none"/><circle cx="8" cy="17" r="2"/><circle cx="18" cy="17" r="2"/></svg>
  <div class="abs cart-count">10</div>
</div>

<h1 class="abs hero-title"><span class="lead">A Temple of Traditional</span><span class="main">Cannabis Craftsmanship</span></h1>

<article class="abs feature" style="left:92px" role="img" aria-label="Smoky photograph of a person behind a cannabis tile">
  <div class="feature-frame"><h3>Cannabis</h3><p>The go to place to discover<br>and taste fine cannabis</p></div>
</article>
<article class="abs feature" style="left:434px" role="img" aria-label="Photograph of a box of cigars behind a lounge tile">
  <div class="feature-frame"><h3>Cigar Lounge</h3><p>Regent Hall pairs<br>notable cigar offerings</p></div>
</article>
<article class="abs feature" style="left:776px" role="img" aria-label="Smoky photograph of a person behind a cannabis tile">
  <div class="feature-frame"><h3>Cannabis</h3><p>The go to place to discover<br>and taste fine cannabis</p></div>
</article>

<h2 class="abs section-title" style="top:876px"><span class="kicker mixed">Try them out right now</span><span class="head">Our Beloved Products</span></h2>

<div class="abs grid" style="top:1006px">
  <div class="card"><div class="card-photo tone-wood" role="img" aria-label="Wooden humidor box"></div><div class="card-name">Marcelleros</div><div class="card-price">€122.00</div><div class="add-cart"><svg width="18" height="16" viewBox="0 0 22 20" fill="#fff"><path d="M0 1h4l3 11h12l3-9H6" stroke="#fff" stroke-width="2" fill="none"/><circle cx="8" cy="17" r="2"/><circle cx="18" cy="17" r="2"/></svg></div></div>
  <div class="card"><div class="card-photo tone-cigar" role="img" aria-label="Single banded cigar"></div><div class="card-name">Marcelleros</div><div class="card-price">€122.00</div><div class="add-cart"><svg width="18" height="16" viewBox="0 0 22 20" fill="#fff"><path d="M0 1h4l3 11h12l3-9H6" stroke="#fff" stroke-width="2" fill="none"/><circle cx="8" cy="17" r="2"/><circle cx="18" cy="17" r="2"/></svg></div></div>
  <div class="card"><div class="card-photo tone-pale" role="img" aria-label="White pre-roll tube"></div><div class="card-name">Marcelleros</div><div class="card-price">€122.00</div><div class="add-cart"><svg width="18" height="16" viewBox="0 0 22 20" fill="#fff"><path d="M0 1h4l3 11h12l3-9H6" stroke="#fff" stroke-width="2" fill="none"/><circle cx="8" cy="17" r="2"/><circle cx="18" cy="17" r="2"/></svg></div></div>
  <div class="card"><div class="card-photo tone-berry" role="img" aria-label="Stack of dark edible cubes"></div><div class="card-name">Marcelleros</div><div class="card-price">€122.00</div><div class="add-cart"><svg width="18" height="16" viewBox="0 0 22 20" fill="#fff"><path d="M0 1h4l3 11h12l3-9H6" stroke="#fff" stroke-width="2" fill="none"/><circle cx="8" cy="17" r="2"/><circle cx="18" cy="17" r="2"/></svg></div></div>
  <div class="card"><div class="card-photo tone-cigar" role="img" aria-label="Three chocolate bar packages"></div><div class="card-name">Marcelleros</div><div class="card-price">€122.00</div><div class="add-cart"><svg width="18" height="16" viewBox="0 0 22 20" fill="#fff"><path d="M0 1h4l3 11h12l3-9H6" stroke="#fff" stroke-width="2" fill="none"/><circle cx="8" cy="17" r="2"/><circle cx="18" cy="17" r="2"/></svg></div></div>
  <div class="card"><div class="card-photo tone-leaf" role="img" aria-label="Pile of dried cannabis flower"></div><div class="card-name">Marcelleros</div><div class="card-price">€122.00</div><div class="add-cart"><svg width="18" height="16" viewBox="0 0 22 20" fill="#fff"><path d="M0 1h4l3 11h12l3-9H6" stroke="#fff" stroke-width="2" fill="none"/><circle cx="8" cy="17" r="2"/><circle cx="18" cy="17" r="2"/></svg></div></div>
  <div class="card"><div class="card-photo tone-cigar" role="img" aria-label="Single pointed cigar"></div><div class="card-name">Marcelleros</div><div class="card-price">€122.00</div><div class="add-cart"><svg width="18" height="16" viewBox="0 0 22 20" fill="#fff"><path d="M0 1h4l3 11h12l3-9H6" stroke="#fff" stroke-width="2" fill="none"/><circle cx="8" cy="17" r="2"/><circle cx="18" cy="17" r="2"/></svg></div></div>
  <div class="card"><div class="card-photo tone-amber" role="img" aria-label="Open humidor with cigars"></div><div class="card-name">Marcelleros</div><div class="card-price">€122.00</div><div class="add-cart"><svg width="18" height="16" viewBox="0 0 22 20" fill="#fff"><path d="M0 1h4l3 11h12l3-9H6" stroke="#fff" stroke-width="2" fill="none"/><circle cx="8" cy="17" r="2"/><circle cx="18" cy="17" r="2"/></svg></div></div>
</div>

<section class="abs vape-photo" role="img" aria-label="Black and white photograph of a person exhaling vapor while holding a vape pen"></section>
<div class="abs vape-copy">
  <h2>Vellum Disposable<strong>Vape Pen</strong></h2>
  <p>Combining the best hardware with the purest oil, VELLUM aims to introduce a higher level of standard in the vaping industry.</p>
  <p>CO2 extraction does not deactivate the plant terpenes and cannabinoids making it the highest quality oil on the market. This Disposable Pen features a Rechargeable Lithium Battery and&nbsp; Top-Airflow Ceramic Cartridge.</p>
</div>

<h2 class="abs section-title" style="top:2380px"><span class="kicker">What's Popular</span><span class="head">At Harbor Velvet</span></h2>

<div class="abs grid" style="top:2501px">
  <div class="card"><div class="card-photo tone-sage" role="img" aria-label="CBD cooling spray bottle"></div><div class="card-name">Marcelleros</div><div class="card-price">€122.00</div><div class="add-cart"><svg width="18" height="16" viewBox="0 0 22 20" fill="#fff"><path d="M0 1h4l3 11h12l3-9H6" stroke="#fff" stroke-width="2" fill="none"/><circle cx="8" cy="17" r="2"/><circle cx="18" cy="17" r="2"/></svg></div></div>
  <div class="card"><div class="card-photo tone-wood" role="img" aria-label="Three CBD oil dropper bottles"></div><div class="card-name">Marcelleros</div><div class="card-price">€122.00</div><div class="add-cart"><svg width="18" height="16" viewBox="0 0 22 20" fill="#fff"><path d="M0 1h4l3 11h12l3-9H6" stroke="#fff" stroke-width="2" fill="none"/><circle cx="8" cy="17" r="2"/><circle cx="18" cy="17" r="2"/></svg></div></div>
  <div class="card"><div class="card-photo tone-char" role="img" aria-label="Dark jar of CBD gummies"></div><div class="card-name">Marcelleros</div><div class="card-price">€122.00</div><div class="add-cart"><svg width="18" height="16" viewBox="0 0 22 20" fill="#fff"><path d="M0 1h4l3 11h12l3-9H6" stroke="#fff" stroke-width="2" fill="none"/><circle cx="8" cy="17" r="2"/><circle cx="18" cy="17" r="2"/></svg></div></div>
  <div class="card"><div class="card-photo tone-wood" role="img" aria-label="Wooden humidor box"></div><div class="card-name">Marcelleros</div><div class="card-price">€122.00</div><div class="add-cart"><svg width="18" height="16" viewBox="0 0 22 20" fill="#fff"><path d="M0 1h4l3 11h12l3-9H6" stroke="#fff" stroke-width="2" fill="none"/><circle cx="8" cy="17" r="2"/><circle cx="18" cy="17" r="2"/></svg></div></div>
</div>

<section class="abs roots" role="img" aria-label="Dark sepia background of cannabis leaves"></section>
<div class="abs roots-video" role="img" aria-label="Video still of loose tobacco bundles">
  <div class="play"><svg width="30" height="34" viewBox="0 0 30 34" fill="#fff"><path d="M2 2l26 15L2 32z"/></svg></div>
</div>
<div class="abs roots-copy">
  <h2>Our roots run<strong>Deep at Harbor Velvet</strong></h2>
  <p>Originating from the Kootenay region of British Columbia, our collective of growers have been at the forefront of the BC craft cannabis industry since the early 1990s. Throughout the years, our cultivars have been featured in compassion clubs and dispensaries across the country. At Harbor Velvet, we offer our finest genetics and flowers direct-to-consumer, as well as cannabis derivatives from BC's best producers.</p>
</div>

<footer class="abs footer">
  <h4 style="left:92px">Harbor Velvet</h4>
  <p class="footer-about">Originating from the Kootenay region of British Columbia, our collective of growers have been at the forefront of the BC craft cannabis industry since the early 1990s. Throughout the years, our cultivars have been featured in compassion clubs and dispensaries across the country.</p>
  <h4 style="left:550px">Connect</h4>
  <div class="contact" style="top:130px"><svg width="14" height="14" viewBox="0 0 14 14" fill="#d6a57a"><path d="M3 0l3 3-2 2c1 2 3 4 5 5l2-2 3 3-2 3C6 14 0 8 0 3z"/></svg>+1 855 000 4172</div>
  <div class="contact" style="top:173px"><svg width="14" height="11" viewBox="0 0 14 11" fill="none" stroke="#d6a57a"><rect x=".5" y=".5" width="13" height="10"/><path d="M.5.5 7 6l6.5-5.5"/></svg>info@harborvelvet.com</div>
  <div class="contact" style="top:216px"><svg width="14" height="14" viewBox="0 0 14 14" fill="none" stroke="#d6a57a"><circle cx="7" cy="7" r="6"/><path d="M7 3v4h3"/></svg>Everyday : 10AM TO 7PM</div>
  <h4 style="left:860px">Stay on top</h4>
  <p class="news">Get the latest news, products and<br>more from your friends at Harbor Velvet.</p>
  <div class="signup">SIGN UP</div>
  <div class="socials"><span></span><span></span><span></span><span></span></div>
  <p class="copyright">© 2012-2020&nbsp; HarborVelvet | All Rights Reserved</p>
</footer>

</body>
</html>
```